Recruitment website for new startup company - Calder Ashby Recruitment

Hi , I need to design a web page for my new recruitment company with the ability to link to social media accounts. The ability to add and remove job posts along with a blog page which I can update. More importantly I need the website to have the functionality of applicants being able to upload their cv and somewhere for me to store it. I will need assistance/recommendation for email address with company name, hosting and security. An about us page. The website will also need a search function for applicants to narrow down the search. Again I will need to be able to update this myself as the company grows. I have my logo ready domain address ready and would like the web site done ASAP. Thank you for your help.
Updates

Reason: Want to get a few more ideas and variations to designs done. But using logo as inspiration Thanks

Target Market(s)

Financial and property industry so professionals. New starters to senior management age range 25-60

Industry/Entity Type

Financial

Coding

Coded - Design and coding required

Number of Pages Required

4 page

Colors

Designer to choose colors to be used in the design.

Requirements
Must have
• Ability for me to add amend and remove job posts, ability for applicants to upload cv and for me to store and access it. Link to social media accounts
Should not have
• Needs to be clean approachable so not to childish but must come across as approachable and trustworthy.
• No yellow please my logo has a gold V not yellow. If it looks yellow use a different colour please. Thanks

```html
<!DOCTYPE html>
<html lang="en">
<head>
<meta charset="utf-8">
<title>Calder Ashby Recruitment</title>
<link rel="stylesheet" href="https://fonts.googleapis.com/css2?family=Open+Sans:wght@400;600&family=Roboto+Condensed:wght@400&display=swap">
<style>
:root{
  --blue:#1f4aa6;
  --blue-deep:#183c8c;
  --navy:#0f2a66;
  --gold:#a8864a;
  --gold-dark:#957437;
  --gold-pale:#d9c7a0;
  --ink:#222;
  --muted:#555;
  --link:#2f6fb3;
  --line:#dcdcdc;
  --footer:#202020;
  --white:#fff;
}
*{box-sizing:border-box;margin:0;padding:0}
html,body{width:667px;height:1200px;overflow:hidden}
body{position:relative;background:var(--white);font-family:"Open Sans",Arial,sans-serif;color:var(--ink)}
.abs{position:absolute}

/* hero */
.hero{position:absolute;left:0;top:0;width:667px;height:370px}
.hero-bg{position:absolute;left:0;top:0;width:667px;height:370px}
.brand{left:50px;top:30px;color:var(--white);font-weight:400;line-height:1}
.brand .name{font-size:18px;letter-spacing:1px}
.brand .sub{font-size:9.5px;letter-spacing:3.2px;margin-top:5px}
.nav a{position:absolute;top:47px;color:var(--white);font-size:10.5px;text-decoration:none}
.upload{position:absolute;left:558px;top:42px;width:60px;height:23px;border:1px solid var(--white);border-radius:2px;color:var(--white);font-size:10px;line-height:21px;text-align:center}
.hero-title{left:0;width:667px;top:124px;text-align:center;color:var(--white);font-family:"Roboto Condensed",Arial,sans-serif;font-size:21px;font-weight:400}
.hero-sub{left:0;width:667px;top:157px;text-align:center;color:var(--white);font-family:"Roboto Condensed",Arial,sans-serif;font-size:10px}
.search-panel{left:102px;top:186px;width:470px;height:48px;background:rgba(15,42,102,.75)}
.field{position:absolute;top:10px;height:28px;background:var(--white);border-radius:2px;font-size:8px;color:#444;line-height:28px;padding-left:10px}
.search-btn{position:absolute;left:383px;top:10px;width:77px;height:28px;background:var(--gold);border-radius:2px;color:var(--white);font-size:11px;font-weight:600;text-align:center;line-height:28px}

/* steps */
.intro-title{left:0;width:667px;top:393px;text-align:center;font-size:18px;font-weight:400;color:var(--ink)}
.intro-sub{left:0;width:667px;top:422px;text-align:center;font-size:11.5px;color:#333}
.step{top:474px;width:60px;height:60px;border-radius:50%;background:var(--white);box-shadow:0 0 0 3px #e6f0fb,0 2px 8px rgba(80,140,210,.35)}
.step svg{position:absolute;left:19px;top:19px}
.step-label{top:547px;width:100px;text-align:center;font-size:11px;color:#333}

/* jobs */
.section-title{top:642px;font-size:17.5px;font-weight:400;color:var(--ink)}
.section-rule{top:668px;height:1px;background:#999}
.pager{top:648px}
.job-card{left:50px;width:336px;height:64px;border:1px solid var(--line);background:var(--white);box-shadow:0 1px 2px rgba(0,0,0,.06)}
.job-title{position:absolute;left:15px;font-size:8.5px;color:#333}
.job-loc{position:absolute;left:15px;font-size:7px;color:var(--link)}
.job-time{position:absolute;left:15px;font-size:7px;color:#333}
.job-pay{position:absolute;left:178px;font-size:7px;color:#333;line-height:13px}
.view-btn{position:absolute;left:267px;width:54px;height:19px;border:1px solid var(--link);border-radius:2px;color:var(--link);font-size:6.5px;text-align:center;line-height:17px}
.ico{display:inline-block;vertical-align:-1px;margin-right:2px}

.featured-card{left:415px;top:680px;width:203px;height:248px;border:1px solid var(--line);background:var(--white)}
.featured-photo{position:absolute;left:0;top:0;width:201px;height:91px;background:linear-gradient(100deg,#cfc3b4 0%,#eae6df 40%,#a9b97f 60%,#e7e1d8 80%,#6d7680 100%)}
.featured-card .title{position:absolute;left:12px;top:102px;font-size:8.5px;color:#333}
.featured-card .meta{position:absolute;left:12px;font-size:7px;color:#222}
.featured-card .desc{position:absolute;left:12px;top:170px;width:180px;font-size:7px;line-height:13.5px;color:#555;text-align:justify}
.gold-btn{left:562px;top:938px;width:55px;height:19px;background:var(--gold);border-radius:2px;color:var(--white);font-size:6.5px;text-align:center;line-height:19px}

/* footer */
.footer{left:0;top:1014px;width:667px;height:186px;background:var(--footer);color:var(--white)}
.foot-head{position:absolute;top:42px;font-size:8.5px}
.foot-list{position:absolute;top:64px;list-style:none;font-size:6.5px;line-height:13px}
.foot-contact{position:absolute;left:180px;top:64px;font-size:6.5px;line-height:13px}
.foot-contact .row{position:relative;padding-left:10px}
.foot-contact svg{position:absolute;left:0;top:3px}
.mail-text{position:absolute;left:352px;top:64px;width:120px;font-size:6.5px;line-height:9px}
.mail-form{position:absolute;left:352px;top:86px;width:113px;height:16px;background:var(--white);font-size:6px;line-height:16px;color:#888;padding-left:5px}
.mail-form .go{position:absolute;right:0;top:0;width:34px;height:16px;background:var(--gold);color:var(--white);text-align:center}
.social{position:absolute;top:74px;width:14px;height:14px;border-radius:2px;background:var(--white)}
.foot-rule{position:absolute;left:36px;top:139px;width:568px;height:1px;background:#3a3a3a}
.copyright{position:absolute;left:0;width:667px;top:159px;text-align:center;font-size:6.5px}
</style>
</head>
<body>

<header class="hero">
  <svg class="hero-bg" width="667" height="370" viewBox="0 0 667 370" role="img" aria-label="Photo of business people seated in an office, tinted blue">
    <defs>
      <linearGradient id="heroTint" x1="0" y1="0" x2="1" y2="1">
        <stop offset="0" stop-color="#2552b0"/>
        <stop offset=".5" stop-color="#1e48a2"/>
        <stop offset="1" stop-color="#1a3f93"/>
      </linearGradient>
    </defs>
    <path d="M0 0H667V306Q333 404 0 306Z" fill="var(--gold-pale)" transform="translate(0 14)"/>
    <path d="M0 0H667V306Q333 396 0 306Z" fill="var(--gold)" transform="translate(0 6)"/>
    <path d="M0 0H667V306Q333 396 0 306Z" fill="url(#heroTint)"/>
  </svg>

  <div class="brand abs">
    <div class="name">CALDER ASHBY</div>
    <div class="sub">RECRUITMENT</div>
  </div>

  <nav class="nav">
    <a style="left:252px">Home</a>
    <a style="left:307px">About</a>
    <a style="left:362px">Recruitment</a>
    <a style="left:446px">News</a>
    <a style="left:499px">Contact</a>
    <span class="upload">Upload cv</span>
  </nav>

  <h1 class="hero-title abs">Multi-Industry Recruitment Agency</h1>
  <p class="hero-sub abs">Select your sector and/or type job keywords, then click search to find your perfect job</p>

  <svg class="abs" style="left:34px;top:172px" width="13" height="13" viewBox="0 0 13 13"><circle cx="6.5" cy="6.5" r="6.5" fill="var(--navy)"/><path d="M7.5 4L5 6.5 7.5 9" stroke="#fff" stroke-width="1.3" fill="none"/></svg>
  <svg class="abs" style="left:618px;top:165px" width="13" height="13" viewBox="0 0 13 13"><circle cx="6.5" cy="6.5" r="6.5" fill="var(--navy)"/><path d="M5.5 4L8 6.5 5.5 9" stroke="#fff" stroke-width="1.3" fill="none"/></svg>

  <form class="search-panel abs">
    <div class="field" style="left:13px;width:118px">Job Keywords</div>
    <div class="field" style="left:136px;width:119px">Location
      <svg class="abs" style="right:9px;top:12px" width="7" height="5" viewBox="0 0 7 5"><path d="M.5.5L3.5 3.5 6.5.5" stroke="#444" fill="none"/></svg></div>
    <div class="field" style="left:260px;width:118px">Sector
      <svg class="abs" style="right:9px;top:12px" width="7" height="5" viewBox="0 0 7 5"><path d="M.5.5L3.5 3.5 6.5.5" stroke="#444" fill="none"/></svg></div>
    <div class="search-btn">Search</div>
  </form>
</header>

<section>
  <h2 class="intro-title abs">All the jobs you want in one simple place</h2>
  <p class="intro-sub abs">Find the jobs you want in just a few simple quicks</p>

  <div class="step abs" style="left:157px">
    <svg width="22" height="22" viewBox="0 0 22 22"><circle cx="9" cy="9" r="6" stroke="var(--blue)" stroke-width="3" fill="none"/><path d="M13.5 13.5L19 19" stroke="var(--blue)" stroke-width="3.5" stroke-linecap="round"/></svg>
  </div>
  <div class="step abs" style="left:300px">
    <svg width="22" height="22" viewBox="0 0 22 22"><path d="M4 18l1-5 9-9 4 4-9 9z" fill="var(--blue)"/><path d="M15 3l4 4" stroke="#fff" stroke-width="1"/></svg>
  </div>
  <div class="step abs" style="left:448px">
    <svg width="22" height="22" viewBox="0 0 22 22"><circle cx="11" cy="6.5" r="4.5" fill="var(--blue)"/><path d="M3 20c0-5 3.5-8 8-8s8 3 8 8z" fill="var(--blue)"/></svg>
  </div>
  <div class="step-label abs" style="left:137px">SEARCH</div>
  <div class="step-label abs" style="left:280px">APPLY</div>
  <div class="step-label abs" style="left:428px">HIRED</div>
</section>

<section>
  <h3 class="section-title abs" style="left:48px">Recent Jobs</h3>
  <div class="section-rule abs" style="left:48px;width:339px"></div>
  <svg class="pager abs" style="left:367px" width="20" height="11" viewBox="0 0 20 11"><path d="M7 1L2 5.5 7 10M13 1l5 4.5L13 10" stroke="#333" stroke-width="2" fill="none"/></svg>

  <h3 class="section-title abs" style="left:414px">Featured Job</h3>
  <div class="section-rule abs" style="left:414px;width:203px"></div>
  <svg class="pager abs" style="left:598px" width="20" height="11" viewBox="0 0 20 11"><path d="M7 1L2 5.5 7 10M13 1l5 4.5L13 10" stroke="#333" stroke-width="2" fill="none"/></svg>

  <article class="job-card abs" style="top:681px">
    <div class="job-title" style="top:12px">Seles&amp; Marketing Coordinator</div>
    <div class="job-loc" style="top:28px"><svg class="ico" width="5" height="7" viewBox="0 0 5 7"><path d="M2.5 7L.3 3.3A2.5 2.5 0 1 1 4.7 3.3z" fill="var(--link)"/></svg>Germany, Hanover</div>
    <div class="job-time" style="top:42px"><svg class="ico" width="7" height="7" viewBox="0 0 7 7"><circle cx="3.5" cy="3.5" r="2.8" stroke="#222" fill="none"/><path d="M3.5 2v1.7h1.3" stroke="#222" fill="none" stroke-width=".8"/></svg>65 days 21:46:59</div>
    <div class="job-pay" style="top:20px">£27500<br>Full time</div>
    <div class="view-btn" style="top:21px">View More</div>
  </article>

  <article class="job-card abs" style="top:750px">
    <div class="job-title" style="top:12px">ENGINEERING TECHNICIAN</div>
    <div class="job-loc" style="top:28px"><svg class="ico" width="5" height="7" viewBox="0 0 5 7"><path d="M2.5 7L.3 3.3A2.5 2.5 0 1 1 4.7 3.3z" fill="var(--link)"/></svg>Netherlands, Rotterdam</div>
    <div class="job-time" style="top:42px"><svg class="ico" width="7" height="7" viewBox="0 0 7 7"><circle cx="3.5" cy="3.5" r="2.8" stroke="#222" fill="none"/><path d="M3.5 2v1.7h1.3" stroke="#222" fill="none" stroke-width=".8"/></svg>42 days 20:41:55</div>
    <div class="job-pay" style="top:20px">£27500<br>Full time</div>
    <div class="view-btn" style="top:21px">View More</div>
  </article>

  <article class="job-card abs" style="top:818px">
    <div class="job-title" style="top:21px">SCIENCE TEACHER</div>
    <div class="job-loc" style="top:37px"><svg class="ico" width="5" height="7" viewBox="0 0 5 7"><path d="M2.5 7L.3 3.3A2.5 2.5 0 1 1 4.7 3.3z" fill="var(--link)"/></svg>Englond, London, Camden</div>
    <div class="job-pay" style="top:20px">£27500<br>Full time</div>
    <div class="view-btn" style="top:21px">View More</div>
  </article>

  <article class="job-card abs" style="top:888px">
    <div class="job-title" style="top:21px">ACCOUNTS ASSISTANT</div>
    <div class="job-loc" style="top:37px"><svg class="ico" width="5" height="7" viewBox="0 0 5 7"><path d="M2.5 7L.3 3.3A2.5 2.5 0 1 1 4.7 3.3z" fill="var(--link)"/></svg> England, Hampsire, Gosport</div>
    <div class="job-pay" style="top:20px">£27500<br>Full time</div>
    <div class="view-btn" style="top:21px">View More</div>
  </article>

  <article class="featured-card abs">
    <div class="featured-photo" role="img" aria-label="Photo of a job interview handshake in an office"></div>
    <div class="title">STEAK HOUSE MANAGER</div>
    <div class="meta" style="top:118px">Netherlands, Rotterdam</div>
    <div class="meta" style="top:132px">£27500 - £30000</div>
    <div class="meta" style="top:146px">Full time</div>
    <p class="desc">Lorem Ipsum has been the industry's standard dummy text ever since the 1500s, when an unknown printer took a galley of type and scrambled it to make a type specimen book.</p>
  </article>
  <div class="gold-btn abs">View More</div>
</section>

<footer class="footer abs">
  <div class="foot-head" style="left:56px">QUICK LINKS</div>
  <ul class="foot-list" style="left:57px">
    <li>» Services</li><li>» About Us</li><li>» Search</li><li>» Contact Us</li>
  </ul>

  <div class="foot-head" style="left:180px">CONTACT US</div>
  <div class="foot-contact">
    <div class="row"><svg width="5" height="7" viewBox="0 0 5 7"><path d="M2.5 7L.3 3.3A2.5 2.5 0 1 1 4.7 3.3z" fill="#fff"/></svg>48 Wren Lane, Ardmore VIC<br>3190, Australia</div>
    <div class="row" style="margin-top:4px"><svg width="6" height="6" viewBox="0 0 6 6"><path d="M1 0h1.3l.6 1.6-.8.6a4 4 0 0 0 1.7 1.7l.6-.8L6 3.7V5a1 1 0 0 1-1 1A5 5 0 0 1 0 1a1 1 0 0 1 1-1z" fill="#fff"/></svg>03 5550 1742</div>
    <div class="row" style="margin-top:4px"><svg width="7" height="5" viewBox="0 0 7 5"><rect width="7" height="5" fill="#fff"/><path d="M0 0l3.5 2.7L7 0" stroke="#202020" stroke-width=".8" fill="none"/></svg>hello@calderashby.example</div>
  </div>

  <div class="foot-head" style="left:352px">JOIN OUR MAILING LIST</div>
  <p class="mail-text">Your about us information would fit here nicely.</p>
  <div class="mail-form">Email address<span class="go">Submit</span></div>

  <div class="foot-head" style="left:514px">FOLLOW US OUT THERE</div>
  <span class="social" style="left:514px"></span>
  <span class="social" style="left:536px"></span>
  <span class="social" style="left:557px"></span>
  <span class="social" style="left:579px"></span>

  <div class="foot-rule"></div>
  <p class="copyright">Copyright © 2017 All Rights Reserved &nbsp;| Privacy | Terms and conditions</p>
</footer>

</body>
</html>
```